Ferncrest Dental, LLC business card project

Business card to be designed with current logo.
Dental office- please keep design of card that looks clean and professional.
Please include the following info:
Ferncrest Dental, LLC
Dr. Lorna Pettigrew
2871 Marlowe Street
Bethlehem, PA 18093
610-555-0193
ferncrestdental.office@examplemail.test
Hello everyone-
Reason: Just got back from overseas- will look at all designs and provide feedback. Thank you!
Reason: Polling my friends for the final selection-
thank you to all those that participated- so many talented designers!

```html
<!DOCTYPE html>
<html lang="en">
<head>
<meta charset="utf-8">
<title>Ferncrest Dental, LLC — Business Card</title>
<link href="https://fonts.googleapis.com/css2?family=Quicksand:wght@400;500&display=swap" rel="stylesheet">
<style>
  :root {
    --page-bg: #e4e4e4;
    --panel-dark: #222222;
    --panel-grey-light: #5e5e5e;
    --panel-grey-dark: #3f3f3f;
    --lime: #a6cf2f;
    --edge: #d9e3b0;
    --watermark: rgba(255, 255, 255, 0.09);
  }
  * { box-sizing: border-box; margin: 0; padding: 0; }
  html, body {
    width: 1200px;
    height: 981px;
    overflow: hidden;
    background: var(--page-bg);
    font-family: "Quicksand", sans-serif;
  }
  .canvas {
    position: relative;
    width: 1200px;
    height: 981px;
  }
  .card {
    position: absolute;
    left: 100px;
    top: 190px;
    width: 1000px;
    height: 602px;
    border: 3px solid var(--edge);
    background: linear-gradient(90deg, var(--panel-grey-light) 0%, var(--panel-grey-dark) 55%, var(--panel-grey-light) 100%);
    box-shadow: 0 10px 30px rgba(0, 0, 0, 0.35);
    overflow: hidden;
  }
  .card__side-panel {
    position: absolute;
    left: 0;
    top: 0;
    width: 390px;
    height: 100%;
    background: var(--panel-dark);
  }
  .brand-plate {
    position: absolute;
    left: 10px;
    top: 252px;
    width: 510px;
    height: 100px;
    background: var(--panel-dark);
    border: 2px solid var(--edge);
    box-shadow: 0 6px 14px rgba(0, 0, 0, 0.55);
    display: flex;
    align-items: center;
    padding-left: 30px;
    gap: 18px;
  }
  .brand-plate__dot {
    width: 26px;
    height: 26px;
    border-radius: 50%;
    background: var(--lime);
    flex: none;
  }
  .brand-plate__name {
    color: var(--lime);
    font-size: 40px;
    font-weight: 500;
    white-space: nowrap;
  }
  .card__name {
    position: absolute;
    left: 560px;
    top: 272px;
    color: var(--lime);
    font-size: 44px;
    font-weight: 500;
    white-space: nowrap;
  }
  .contact {
    position: absolute;
    left: 0;
    top: 496px;
    width: 390px;
    text-align: center;
    color: var(--lime);
    font-size: 17px;
    line-height: 27px;
    font-weight: 400;
  }
  .card__watermark {
    position: absolute;
    left: 430px;
    top: 520px;
    color: var(--watermark);
    font-size: 44px;
    font-weight: 500;
    white-space: nowrap;
  }
</style>
</head>
<body>
  <main class="canvas">
    <article class="card">
      <div class="card__side-panel"></div>

      <div class="brand-plate">
        <span class="brand-plate__dot"></span>
        <span class="brand-plate__name">Ferncrest Dental, LLC</span>
      </div>

      <h1 class="card__name">Dr. Lorna Pettigrew</h1>

      <address class="contact" style="font-style: normal;">
        <p>2871 Marlowe Street Bethlehem, PA 18093</p>
        <p>ferncrestdental.office@examplemail.test</p>
        <p>tel. 610-555-0193</p>
      </address>

      <p class="card__watermark" aria-hidden="true">Ferncrest Dental, LLC</p>
    </article>
  </main>
</body>
</html>
```